wedding invitation card

Requirement:
1. White background, pink elements on the card, simple elegant looking
2. content:
Please join us as we celebrate new beginnings, new dreams,
and most importantly, new love at the marriage of
Miss Lin Qiao and Mr. Haoran Bei
Friday, The First of January
Two Thousand Fifteen at Eleven o’clock
Coral Breeze Hotel Palm Garden Deck.

Reception will be followed at Lantern Hall at Half-Past Twelve o'clock

Please RSVP before December 18th 2015 by email: qiaolin0317@mailnest.example

3. Flat paper
4. be able to change the size of the design according to printing requirement

```html
<!DOCTYPE html>
<html lang="en">
<head>
<meta charset="utf-8">
<title>Wedding Invitation – Lin Qiao &amp; Haoran Bei</title>
<link rel="stylesheet" href="https://fonts.googleapis.com/css2?family=Pinyon+Script&family=Noto+Sans:wght@400&display=swap">
<style>
  :root {
    --paper: #ffffff;
    --ink: #000000;
    --rose: #f25fd8;
    --leaf-light: #f9b3e4;
    --leaf-deep: #f07ccf;
    --card-w: 1200px;
    --card-h: 927px;
  }
  * { margin: 0; padding: 0; box-sizing: border-box; }
  html, body {
    width: var(--card-w);
    height: var(--card-h);
    overflow: hidden;
    background: var(--paper);
  }
  .invitation {
    position: relative;
    width: var(--card-w);
    height: var(--card-h);
    background: var(--paper);
    color: var(--ink);
  }
  .invitation__frame {
    position: absolute;
    left: 53px;
    top: 66px;
    width: 1092px;
    height: 792px;
    border: 2px solid var(--rose);
  }
  .script {
    font-family: "Pinyon Script", cursive;
    font-weight: 400;
    text-align: center;
    position: absolute;
    left: 0;
    width: 100%;
  }
  .welcome {
    top: 112px;
    font-size: 42px;
    line-height: 64px;
  }
  .couple {
    position: absolute;
    top: 330px;
    left: 0;
    width: 100%;
    display: flex;
    justify-content: center;
    align-items: center;
    font-family: "Noto Sans", sans-serif;
    font-weight: 400;
    font-size: 61px;
    line-height: 1;
    white-space: nowrap;
  }
  .couple__name { position: relative; z-index: 1; }
  .couple__amp {
    font-family: "Pinyon Script", cursive;
    font-weight: 400;
    color: var(--rose);
    font-size: 128px;
    line-height: 1;
    margin: -10px -14px 0 -10px;
    position: relative;
    z-index: 0;
  }
  .date {
    top: 486px;
    font-size: 44px;
    line-height: 66px;
  }
  .details {
    position: absolute;
    left: 100px;
    top: 684px;
    font-family: "Noto Sans", sans-serif;
    font-size: 16.5px;
    line-height: 1.4;
  }
  .details p { margin-bottom: 26px; }
  .sprig {
    position: absolute;
    border-radius: 50% 40% 50% 45%;
    background: radial-gradient(circle at 50% 55%, var(--leaf-deep), var(--leaf-light) 70%, rgba(249,179,228,0) 100%);
    opacity: 0.85;
  }
  .sprig--left { left: 28px; top: 810px; width: 108px; height: 62px; }
  .sprig--right { left: 1022px; top: 734px; width: 140px; height: 128px; }
</style>
</head>
<body>
  <main class="invitation">
    <div class="invitation__frame"></div>

    <p class="script welcome">Please join us as we celebrate new beginnings, new dreams,<br>and most importantly, new love at the marriage of</p>

    <h1 class="couple">
      <span class="couple__name">Miss Lin Qiao</span>
      <span class="couple__amp">&amp;</span>
      <span class="couple__name">Mr. Haoran Bei</span>
    </h1>

    <p class="script date">Friday, The First of January<br>Two Thousand Fifteen at Eleven o’clock</p>

    <section class="details">
      <p>Coral Breeze Hotel Palm Garden Deck.</p>
      <p>Reception will be followed at Lantern Hall at Half-Past Twelve o'clock</p>
      <p>Please RSVP before December 18th 2015 by email: qiaolin0317@mailnest.example</p>
    </section>

    <div class="sprig sprig--left" role="img" aria-label="Pink leaf sprig ornament"></div>
    <div class="sprig sprig--right" role="img" aria-label="Pink leaf sprig ornament"></div>
  </main>
</body>
</html>
```